Young Accounting firm needing a captivating business card

We need a business card design that forces the person to look at the card because its either gold foil, plastic, or lettering pop up etc. We already have a logo with a specific gold color and we need to make it pop. We are an accounting firm. I need the words" accounting, payroll, licenses, audits, taxes" somewhere on the business card so as to describe what we do- preferably on the side where the logo is at.

Industry/Entity Type

Accounting

Contact Information for Business Card

Address 48276 9th Ave S Ste 305, Cedar Point, OR 98117
Business Phone (360)418-2096
Fax (360)418-2157
Office Cell Phone (360)586-7319

Font styles to use
Serif

Colors
85abd2

Requirements
Must have
• It should state
• "Accounting" "Taxes" "Audits" "Licenses" "Payroll"
Nice to have
• Matte with gold foil, different textures, With Either a textured ivory background or gray blue slate background
Should not have
• colorful colors

```html
<!DOCTYPE html>
<html lang="en">
<head>
<meta charset="utf-8">
<title>Harbor Ledger – Business Card</title>
<link rel="stylesheet" href="https://fonts.googleapis.com/css2?family=EB+Garamond:wght@400;500;600&display=swap">
<style>
  :root {
    --stage: #e9e6e1;
    --card-dark: #1f1f21;
    --card-light: #ffffff;
    --gold: #b8952a;
    --ink: #1c1c1c;
  }
  * { margin: 0; padding: 0; box-sizing: border-box; }
  html, body { width: 1200px; height: 715px; overflow: hidden; }
  body {
    background: var(--stage);
    font-family: "EB Garamond", Georgia, serif;
    display: flex;
    align-items: center;
    justify-content: center;
    gap: 60px;
  }
  .card {
    width: 520px;
    height: 297px;
    position: relative;
    box-shadow: 0 10px 26px rgba(0,0,0,0.18);
  }

  /* back */
  .card--back { background: var(--card-dark); }
  .back-mark {
    position: absolute;
    top: 96px; left: 0; right: 0;
    display: flex; align-items: center; justify-content: center; gap: 14px;
    color: var(--gold);
    font-size: 40px; font-weight: 500;
  }
  .back-mark .square { width: 22px; height: 22px; background: var(--gold); }
  .back-url {
    position: absolute;
    left: 44px; bottom: 40px;
    color: var(--gold);
    font-size: 13px; letter-spacing: 3px;
  }

  /* front */
  .card--front { background: var(--card-light); }
  .brand {
    position: absolute;
    top: 34px; left: 230px;
    width: 250px;
    text-align: center;
  }
  .brand-name {
    display: flex; align-items: center; justify-content: center; gap: 10px;
    color: var(--gold);
    font-size: 34px; font-weight: 500; line-height: 1;
  }
  .brand-name .square { width: 16px; height: 16px; background: var(--gold); }
  .brand-rule { height: 1.5px; background: var(--gold); margin: 6px 0 4px; }
  .brand-tagline { font-size: 9px; color: var(--ink); letter-spacing: .3px; }

  .divider {
    position: absolute;
    top: 142px; left: 44px; right: 44px;
    height: 2px; background: var(--gold);
  }
  .contact {
    position: absolute;
    top: 160px; left: 44px;
    list-style: none;
    font-size: 13.5px; color: var(--ink);
  }
  .contact li { display: flex; align-items: center; gap: 10px; height: 22px; }
  .contact svg { width: 12px; height: 12px; fill: var(--gold); flex: none; }

  .person {
    position: absolute;
    top: 158px; right: 44px;
    text-align: left;
  }
  .person-name { color: var(--gold); font-size: 17px; }
  .person-title { color: var(--ink); font-size: 15px; font-weight: 500; }

  .address {
    position: absolute;
    right: 44px; bottom: 30px;
    color: var(--gold);
    font-size: 15px; font-weight: 500; line-height: 1.25;
    font-style: normal;
  }
</style>
</head>
<body>

  <section class="card card--back">
    <div class="back-mark"><span class="square"></span><span>Harbor Ledger</span></div>
    <div class="back-url">www.harborledger.com</div>
  </section>

  <section class="card card--front">
    <header class="brand">
      <div class="brand-name"><span class="square"></span><span>Harbor Ledger</span></div>
      <div class="brand-rule"></div>
      <div class="brand-tagline">Accounting, Payroll, Licenses, Audits, Taxes</div>
    </header>

    <div class="divider"></div>

    <ul class="contact">
      <li>
        <svg viewBox="0 0 12 12" aria-hidden="true"><path d="M1 4c0-1.5 2-2.5 5-2.5S11 2.5 11 4v1H8.5V3.8h-5V5H1z M2.5 6h7l1 4.5h-9z"/></svg>
        (360)418-2096
      </li>
      <li>
        <svg viewBox="0 0 12 12" aria-hidden="true"><path d="M3 1h6v3H3z M1 5h10v5H1z M3 8h6v3H3z" fill-rule="evenodd"/></svg>
        (360)418-2157
      </li>
      <li>
        <svg viewBox="0 0 12 12" aria-hidden="true"><path d="M3 1.5l2 2-1.2 1.5c.7 1.5 1.7 2.5 3.2 3.2L8.5 7l2 2-1.5 2C5 10.5 1.5 7 1 3z"/></svg>
        (360)586-7319
      </li>
      <li>
        <svg viewBox="0 0 12 12" aria-hidden="true"><path d="M1 2.5h10v7H1z M1.5 3l4.5 3.5L10.5 3" /></svg>
        nora.whitfield@harborledger.com
      </li>
    </ul>

    <div class="person">
      <div class="person-name">Nora Whitfield</div>
      <div class="person-title">Practise Manager</div>
    </div>

    <address class="address">
      48276 9th Ave S Ste 305<br>
      Cedar Point, OR 98117
    </address>
  </section>

</body>
</html>
```